Birthday Party Flyer

We are a roller skating rink in need of a new birthday flyer. We have used the same flyer format for quite sometime and are looking for something new. This flyer needs to look fun for children and be easy to read for the parents. The information should be presented organized and be easy to read. Please check out our website for more information on our company. www.maplebeam4x.com. Please visit our FB and google account for any additional pictures. Thank You!

Target Market(s)

Needs to appeal to children ages 4-14 and have the information clearly laid out for parents to read and understand.

Colors
0356a4
ec1f27

Requirements
Must have
• Color and a fun design
• Must incorporate our logo
Nice to have
• Feel free to select your own color pallet
Should not have
• Profanity

```html
<!DOCTYPE html>
<html lang="en">
<head>
<meta charset="utf-8">
<title>Birthday Party Flyer</title>
<link href="https://fonts.googleapis.com/css2?family=Nunito:wght@700;800&family=Lato:wght@400;700&display=swap" rel="stylesheet">
<style>
  :root{
    --brand-blue:#0356a4;
    --brand-red:#ec1f27;
    --paper:#f4f4f5;
    --ink:#2b2b2b;
    --white:#ffffff;
    --backdrop:#e6e6e6;
  }
  *{box-sizing:border-box;margin:0;padding:0}
  html,body{width:1200px;height:1200px;overflow:hidden;background:var(--backdrop)}
  .flyer{position:absolute;left:185px;top:20px;width:830px;height:1160px;background:var(--paper);overflow:hidden;font-family:'Lato',sans-serif;color:var(--ink)}
  .flyer-shapes{position:absolute;inset:0}
  .party-photo{position:absolute;left:110px;top:-125px;width:570px;height:570px;border-radius:50%;
    background:radial-gradient(circle at 40% 30%,#6fb3b5 0%,#3e6f86 35%,#b24a84 70%,#e25aa0 100%);
    border:10px solid var(--white);box-shadow:0 0 0 11px var(--brand-blue),0 0 0 38px var(--brand-red)}
  .pill{position:absolute;background:var(--brand-blue);color:var(--white);font-family:'Nunito',sans-serif;font-weight:800;
    font-size:23px;padding:5px 14px 6px;border-radius:14px;border:3px solid var(--white);box-shadow:0 0 0 1px var(--brand-blue);white-space:nowrap}
  .package-list{position:absolute;list-style:none;font-size:14.5px;line-height:19.5px}
  .package-list li{position:relative;padding-left:16px}
  .package-list li::before{content:"";position:absolute;left:0;top:7px;width:7px;height:7px;border-radius:50%;background:var(--brand-red)}
  .schedule{position:absolute;font-size:17.5px;line-height:23px}
  .skate-photo{position:absolute;left:410px;top:790px;width:210px;height:210px;border-radius:50%;border:5px solid var(--white);
    background:radial-gradient(circle at 50% 40%,#e8ddd0 0%,#9a7a66 45%,#b8322a 75%,#3a2a2a 100%)}
  .rink-mark{position:absolute;left:610px;top:765px;width:190px;height:190px;border-radius:50%;background:var(--brand-blue);border:6px solid var(--white);
    display:flex;align-items:center;justify-content:center;text-align:center}
  .rink-name{font-family:'Nunito',sans-serif;font-weight:800;font-size:26px;line-height:28px;color:var(--white)}
  .booking{position:absolute;right:40px;top:995px;text-align:right;color:var(--white)}
  .booking-lead{font-family:'Nunito',sans-serif;font-weight:800;font-size:25px;line-height:28px}
  .booking-site{font-size:22px;line-height:28px}
  .booking-note{font-size:13px;line-height:18px}
  .contact{position:absolute;top:1100px;color:var(--white);font-weight:700;font-size:17px;display:flex;align-items:center;gap:6px}
  .contact svg{fill:var(--white)}
</style>
</head>
<body>
<main class="flyer">
  <svg class="flyer-shapes" viewBox="0 0 830 1160" width="830" height="1160" aria-hidden="true">
    <path d="M0 0H830V390L0 420Z" fill="var(--brand-red)"/>
    <path d="M0 420L830 390V408L0 444Z" fill="var(--white)"/>
    <path d="M0 444L830 408V430L0 472Z" fill="var(--brand-blue)"/>
    <path d="M0 1115C250 990 500 930 830 890V925C500 962 250 1022 0 1142Z" fill="var(--brand-red)"/>
    <path d="M0 1142C250 1022 500 962 830 925V1160H0Z" fill="var(--brand-blue)"/>
  </svg>

  <div class="party-photo" role="img" aria-label="Photo of a birthday girl at a party table with cake and balloons beside the skating rink"></div>

  <h2 class="pill" style="left:100px;top:548px">Deluxe Birthday $175</h2>
  <ul class="package-list" style="left:92px;top:600px">
    <li>12 Admissions</li><li>12 Skate Rentals</li><li>12 Ice cream cups</li><li>2 Hours</li>
    <li>2 Party Tables</li><li>Party Host</li><li>LED Birthday Badge</li>
  </ul>
  <ul class="package-list" style="left:265px;top:596px">
    <li>Birthday Announcement</li><li>$5 Fund Bucks</li><li>1 Month Free Skating Pass</li><li>100 Tokens</li>
    <li>3 Pitchers of Pop</li><li>3 Large Pizza's</li><li>T-shirt for b-day child</li>
  </ul>

  <h2 class="pill" style="left:500px;top:535px">Classic Birthday $140</h2>
  <ul class="package-list" style="left:500px;top:588px">
    <li>12 Admissions</li><li>12 Skate Rentals</li><li>12 Ice cream cups</li><li>2 Hours</li>
    <li>2 Party Tables</li><li>Party Host</li><li>2 Pitchers of Pop</li>
  </ul>
  <ul class="package-list" style="left:650px;top:584px;width:150px">
    <li>LED Birthday Badge</li><li>Birthday Announce-ment</li><li>$5 Fund Bucks</li>
    <li>1 Month Free Skating Pass</li><li>50 Tokens</li>
  </ul>

  <h2 class="pill" style="left:95px;top:770px">Reservation Details</h2>
  <p class="schedule" style="left:110px;top:840px">Saturdays<br>12p.m. to 2p.m.<br>3p.m. to 5p.m.<br>6p.m. to 8p.m.</p>
  <p class="schedule" style="left:265px;top:835px">Sundays<br>1p.m. to 3p.m.</p>

  <div class="skate-photo" role="img" aria-label="Close-up photo of white roller skates with red wheels"></div>

  <div class="rink-mark"><span class="rink-name">Maplebeam<br>Skate</span></div>

  <div class="booking">
    <p class="booking-lead">Book online at</p>
    <p class="booking-site">maplebeam4x.com or at Maplebeam Skate Center</p>
    <p class="booking-note">Payment Required at time of reservation</p>
  </div>

  <p class="contact" style="left:240px;top:1112px">
    <svg width="15" height="15" viewBox="0 0 24 24"><path d="M6.6 10.8a15 15 0 0 0 6.6 6.6l2.2-2.2a1 1 0 0 1 1-.25 11.4 11.4 0 0 0 3.6.57 1 1 0 0 1 1 1V20a1 1 0 0 1-1 1A17 17 0 0 1 3 4a1 1 0 0 1 1-1h3.5a1 1 0 0 1 1 1c0 1.25.2 2.45.57 3.57a1 1 0 0 1-.25 1Z"/></svg>
    555-014-2290
  </p>
  <p class="contact" style="left:435px;top:1088px">
    <svg width="13" height="18" viewBox="0 0 24 32"><path d="M12 0A12 12 0 0 0 0 12c0 9 12 20 12 20s12-11 12-20A12 12 0 0 0 12 0Zm0 17a5 5 0 1 1 0-10 5 5 0 0 1 0 10Z"/></svg>
    Maplebeam Skate Center 48 Orchard Lane
  </p>
</main>
</body>
</html>
```